IT Services company general flyer

Looking for a printable US letter size flyer to give a brief overview of the services we offer. We also partner with another company for their services as well. Please check out our website at www.gizmobykellan.com and click on "Our Services" to learn about our services and visit www.bluefernguard,com and click on services to learn about their services. Several of our services do overlap, so they only need to be on the flyer once. Let me know if this is too much content and we need to weed some out. We do not want Home phone service on this flyer. The basic design of the flyer should mimic similar to the VOIP one you did for me for the colors and logo. Also check out the "Who Choose us" page on www.gizmobykellan.com to include some of that as well.

Target Market(s)

Targeting Small businesses that may not normally have a budget for their IT Services

Industry/Entity Type

It Service

Font styles to use
Serif
Sans Serif

Requirements
Must have
• Must include my logo, phone number and email/website address and must follow the same basic template of my previous flyers.

```html
<!DOCTYPE html>
<html lang="en">
<head>
<meta charset="utf-8">
<title>Gizmo by Kellan – Our Services Flyer</title>
<link rel="stylesheet" href="https://fonts.googleapis.com/css2?family=Open+Sans:wght@400;600;700;800&family=Montserrat:wght@500&display=swap">
<style>
  :root{
    --red:#b3262a;
    --red-dark:#8e1a1d;
    --navy:#172b5a;
    --ink:#0e1730;
    --text:#1c2235;
    --mist:#eeeef0;
    --white:#ffffff;
    --page:#f4f4f4;
  }
  *{margin:0;padding:0;box-sizing:border-box}
  html,body{width:693px;height:1200px;overflow:hidden;background:var(--page)}
  .canvas{position:relative;width:693px;height:1200px;overflow:hidden}
  .flyer{position:absolute;left:0;top:151px;width:944px;height:1222px;transform:scale(0.7341);transform-origin:0 0;background:var(--white);overflow:hidden;font-family:"Open Sans",Arial,sans-serif;color:var(--text)}
  .shapes{position:absolute;left:0;top:0}
  .brand{position:absolute;left:48px;top:48px;display:flex;align-items:center}
  .brand-mark{width:124px;height:124px;background:var(--red)}
  .brand-rule{width:2px;height:165px;background:#c9c9cf;margin:0 22px 0 28px}
  .brand-name{font-family:"Montserrat",sans-serif;font-weight:500;color:var(--navy);line-height:1}
  .brand-name .big{display:block;font-size:62px;letter-spacing:-1px}
  .brand-name .small{display:block;font-size:46px;letter-spacing:-1px}
  .services-title{position:absolute;left:48px;top:436px;font-size:58px;font-weight:800;color:var(--red);letter-spacing:0.5px;line-height:70px}
  .services-lead{position:absolute;left:50px;top:510px;font-size:24px;font-weight:700;color:var(--navy);line-height:32.5px;white-space:nowrap}
  .services-lead em{font-style:normal;color:var(--red)}
  .accent-bar{position:absolute;left:55px;top:658px;display:flex}
  .accent-bar span{height:5px;width:40px;background:var(--red)}
  .accent-bar span+span{width:34px;background:var(--navy)}
  .service-list{position:absolute;left:48px;top:688px;list-style:none}
  .service-list li{display:flex;align-items:center;height:40px;font-size:15.5px;color:var(--text);white-space:nowrap}
  .service-list svg{width:28px;height:28px;flex:none}
  .service-list .sep{width:2px;height:26px;background:var(--navy);margin:0 16px 0 18px}
  .column-rule{position:absolute;left:447px;top:652px;width:2px;height:433px;background:var(--red)}
  .why-title{position:absolute;left:483px;top:677px;height:43px;width:277px;display:flex}
  .why-title .tab{width:39px;background:var(--navy)}
  .why-title h2{flex:1;background:var(--red);color:var(--white);font-size:23px;font-weight:800;line-height:43px;padding-left:14px}
  .reasons{position:absolute;left:483px;top:738px;width:425px;list-style:none}
  .reasons li{position:relative;padding-left:29px;margin-bottom:22px}
  .reasons li::before{content:"";position:absolute;left:4px;top:8px;width:9px;height:9px;background:var(--red)}
  .reasons h3{font-size:19px;font-weight:800;color:var(--navy);line-height:22px}
  .reasons p{font-family:Arial,Helvetica,sans-serif;font-size:15.2px;line-height:17.4px;color:var(--text)}
  .contact-phone{position:absolute;left:50px;top:1132px;display:flex;align-items:center;color:var(--white);font-size:34px;font-weight:800}
  .contact-phone svg,.contact-mail svg,.web svg{margin-right:10px}
  .contact-mail{position:absolute;left:54px;top:1180px;display:flex;align-items:center;color:var(--white);font-size:17px;font-weight:700}
  .web{position:absolute;left:405px;top:1174px;display:flex;align-items:center;color:var(--white);font-size:18px;font-weight:700}
  .social{position:absolute;left:715px;top:1128px;width:229px;text-align:center;color:var(--white)}
  .social .label{font-size:13px;letter-spacing:0.3px}
  .social .dot{width:30px;height:30px;border-radius:50%;background:var(--white);margin:6px auto 4px}
  .social .url{font-size:12px;font-weight:700}
</style>
</head>
<body>
<div class="canvas">
  <div class="flyer">
    <svg class="shapes" width="944" height="1222" viewBox="0 0 944 1222">
      <defs>
        <linearGradient id="redFade" x1="0" y1="0" x2="1" y2="1">
          <stop offset="0" stop-color="#c0302f"/><stop offset="1" stop-color="#8a1a1c"/>
        </linearGradient>
        <linearGradient id="techGlow" x1="0" y1="0" x2="1" y2="1">
          <stop offset="0" stop-color="#0b1426"/><stop offset="0.5" stop-color="#1a5a8c"/><stop offset="1" stop-color="#081226"/>
        </linearGradient>
      </defs>
      <polygon points="0,0 820,0 454,214 204,342 0,236" fill="var(--mist)"/>
      <polygon points="832,0 944,0 944,190 722,68" fill="url(#redFade)"/>
      <polygon points="0,244 185,349 0,454" fill="url(#redFade)"/>
      <polygon points="222,349 439,227 439,459" fill="var(--navy)"/>
      <polygon points="710,69 944,204 944,529 710,659 454,529 454,214" fill="url(#techGlow)" role="img" aria-label="Photo of a hand holding a glowing digital padlock surrounded by connected technology icons"/>
      <polygon points="0,1114 332,1114 382,1222 0,1222" fill="url(#redFade)"/>
      <polygon points="350,1152 700,1152 700,1222 382,1222" fill="var(--navy)"/>
      <polygon points="676,1114 944,1114 944,1222 715,1222" fill="var(--ink)"/>
    </svg>

    <header class="brand">
      <div class="brand-mark"></div>
      <div class="brand-rule"></div>
      <div class="brand-name"><span class="big">GIZMO</span><span class="small">BY KELLAN</span></div>
    </header>

    <h1 class="services-title">Our Services</h1>
    <p class="services-lead">We provide a<br>complete range of <em>IT services</em><br>focused on you getting the most<br>from your technology</p>
    <div class="accent-bar"><span></span><span></span></div>

    <ul class="service-list">
      <li><svg viewBox="0 0 28 28" fill="none" stroke="#b3262a" stroke-width="1.6"><circle cx="14" cy="8" r="5"/><path d="M5 26v-5a9 6 0 0 1 18 0v5z"/></svg><span class="sep"></span>Managed IT Services</li>
      <li><svg viewBox="0 0 28 28" fill="none" stroke="#b3262a" stroke-width="1.6"><path d="M6 6l5 0 2 5-3 2a12 12 0 0 0 5 5l2-3 5 2v5a18 18 0 0 1-16-16z"/></svg><span class="sep"></span>Business VOIP Phone Service</li>
      <li><svg viewBox="0 0 28 28" fill="none" stroke="#b3262a" stroke-width="1.6"><path d="M14 3l9 4v7c0 6-4 9-9 11-5-2-9-5-9-11V7z"/><path d="M10 14l3 3 5-6"/></svg><span class="sep"></span>Security Services with Bluefern Guard</li>
      <li><svg viewBox="0 0 28 28" fill="none" stroke="#b3262a" stroke-width="1.6"><rect x="3" y="4" width="18" height="6" rx="2"/><rect x="3" y="12" width="18" height="6" rx="2"/><path d="M19 17l5 2v4l-5 3-5-3v-4z"/></svg><span class="sep"></span>Network Security</li>
      <li><svg viewBox="0 0 28 28" fill="none" stroke="#b3262a" stroke-width="1.6"><rect x="4" y="17" width="20" height="6" rx="1"/><path d="M8 12a8 8 0 0 1 12 0M5 9a12 12 0 0 1 18 0"/></svg><span class="sep"></span>Wireless Solutions</li>
      <li><svg viewBox="0 0 28 28" fill="none" stroke="#b3262a" stroke-width="1.6"><path d="M8 20a5 5 0 0 1 0-10 7 7 0 0 1 13 2 4 4 0 0 1 0 8z"/></svg><span class="sep"></span>Cloud Services</li>
      <li><svg viewBox="0 0 28 28" fill="none" stroke="#b3262a" stroke-width="1.6"><rect x="5" y="4" width="18" height="20" rx="1"/><path d="M9 10h10M9 14h10M9 18h7"/></svg><span class="sep"></span>Cloud Office Suite Services</li>
      <li><svg viewBox="0 0 28 28" fill="none" stroke="#b3262a" stroke-width="1.6"><circle cx="14" cy="14" r="10"/><rect x="10" y="13" width="8" height="6"/><path d="M11 13v-2a3 3 0 0 1 6 0v2"/></svg><span class="sep"></span>Endpoint Security Services</li>
      <li><svg viewBox="0 0 28 28" fill="none" stroke="#b3262a" stroke-width="1.6"><rect x="6" y="3" width="16" height="6"/><rect x="6" y="11" width="16" height="6"/><rect x="6" y="19" width="16" height="6"/></svg><span class="sep"></span>Backup &amp; Disaster Recovery Services</li>
      <li><svg viewBox="0 0 28 28" fill="none" stroke="#b3262a" stroke-width="1.6"><rect x="3" y="6" width="22" height="14" rx="1"/><path d="M10 24h8M14 20v4M14 9l4 7h-8z"/></svg><span class="sep"></span>Ransomware &amp; Threat Response Services</li>
    </ul>

    <div class="column-rule"></div>

    <div class="why-title"><span class="tab"></span><h2>Why Choose US</h2></div>
    <ul class="reasons">
      <li><h3>Personalized Solutions and Support</h3><p>We know your time is valuable and your technology is critical. That's why we take time to visit with each of our clients and recommend the best solution for them. Your not just another client to us, we want what is best for you.</p></li>
      <li><h3>Experience</h3><p>We have years of experience in both large and small environments. We know what solutions are available and how to implement them in your business. We are constantly working with industry experts with today's changing technology.</p></li>
      <li><h3>One Stop Shop</h3><p>We can help you with all your IT needs, weather it be computer or network security. Phone and Voice needs, or cloud services. Contact us today to discuss how we can help you.ing with industry experts with today's changing technology.</p></li>
    </ul>

    <div class="contact-phone"><svg width="26" height="26" viewBox="0 0 26 26" fill="none" stroke="#fff" stroke-width="2.2"><circle cx="13" cy="13" r="11"/><path d="M8 7h3l1 3-2 1a7 7 0 0 0 4 4l1-2 3 1v3a11 11 0 0 1-10-10z"/></svg>555.014.2096</div>
    <div class="contact-mail"><svg width="20" height="14" viewBox="0 0 20 14" fill="none" stroke="#fff" stroke-width="1.5"><rect x="1" y="1" width="18" height="12"/><path d="M1 1l9 7 9-7"/></svg>sales@gizmobykellan.com</div>
    <div class="web"><svg width="20" height="20" viewBox="0 0 20 20" fill="none" stroke="#fff" stroke-width="1.5"><circle cx="10" cy="10" r="8.5"/><ellipse cx="10" cy="10" rx="4" ry="8.5"/><path d="M1.5 10h17M3 5.5h14M3 14.5h14"/></svg>www.gizmobykellan.com</div>
    <div class="social">
      <div class="label">FOLLOW US ON</div>
      <div class="dot"></div>
      <div class="url">www.facepage.com/gizmobykellan</div>
    </div>
  </div>
</div>
</body>
</html>
```